Vantor Hub Portal Page . It's guarantee project!

We need a clean and professional modern web application portal page
That includes the Login & Application Selection screen

Also, I need to design both Desktop and Mobile sizes.
We have an example design for our target

The application is Jetty Schedule and related data.
Our client is a bit conservative.

Theme color preferred : #00508B (main) #DF0D83 (secondary)

Target Market(s)

Oil & Fuel & Gasoline

Number of Pages Required

2 page

Font styles to use
Sans Serif

Colors
0054AA
0677BA
7BADD7
CADEEF
E8F1F8
E54698
E96AAD
F1A4CE
F9D9EA
FCEFF6

Requirements
Must have
• Login Page & Main Screen

```html
<!DOCTYPE html>
<html lang="en">
<head>
<meta charset="UTF-8">
<title>Vantor Hub — Application Selection</title>
<link rel="stylesheet" href="https://fonts.googleapis.com/css2?family=Roboto:wght@400;500;700;900&display=swap">
<style>
  :root {
    --brand-blue: #00508B;
    --brand-pink: #DF0D83;
    --stage-bg: #eceef0;
    --surface: #ffffff;
    --sidebar-bg: #f4f4f5;
    --divider: #eeeeee;
    --text-main: #1b1b1b;
    --text-muted: #5f6368;
    --radio-off: #c9c9c9;
    --online: #2e9b2e;
  }
  * { box-sizing: border-box; margin: 0; padding: 0; }
  html, body {
    width: 1200px; height: 978px; overflow: hidden;
    background: var(--stage-bg);
    font-family: "Roboto", Arial, sans-serif;
    color: var(--text-main);
  }
  .portal {
    position: absolute; left: 0; top: 150px;
    width: 1200px; height: 678px;
    background: var(--surface);
  }
  .brand {
    position: absolute; left: 66px; top: 42px;
    font-size: 15px; font-weight: 900; letter-spacing: 0.3px;
    color: var(--brand-blue); text-transform: uppercase;
  }
  .user {
    position: absolute; right: 159px; top: 33px;
    text-align: right; line-height: 1.15; white-space: nowrap;
  }
  .user__name { font-size: 13px; color: var(--text-main); }
  .user__email { font-size: 10px; color: var(--brand-blue); margin-top: 4px; }
  .avatar {
    position: absolute; left: 1058px; top: 33px;
    width: 32px; height: 32px; border-radius: 50%;
    background: linear-gradient(160deg, #cfd6e4, #5b73b8);
  }
  .avatar__status {
    position: absolute; right: -2px; top: -2px;
    width: 8px; height: 8px; border-radius: 50%;
    background: var(--online); border: 1.5px solid var(--surface);
  }
  .header-rule {
    position: absolute; left: 47px; top: 73px; width: 1062px; height: 1px;
    background: var(--divider);
  }
  .sidebar {
    position: absolute; left: 47px; top: 74px;
    width: 172px; height: 561px; background: var(--sidebar-bg);
  }
  .nav-item {
    position: absolute; left: 0; top: 23px; width: 172px; height: 37px;
    background: var(--brand-pink); color: #fff;
    display: flex; align-items: center; gap: 12px; padding-left: 18px;
    font-size: 13px; font-weight: 700;
  }
  .mode-switch {
    position: absolute; left: 592px; top: 105px;
    display: flex; align-items: center; gap: 22px;
    font-size: 19px; color: var(--text-muted);
  }
  .mode-switch__option { display: flex; align-items: center; gap: 9px; }
  .radio {
    width: 18px; height: 18px; border-radius: 50%;
    border: 2px solid var(--radio-off); position: relative;
  }
  .radio--checked { border-color: var(--brand-pink); }
  .radio--checked::after {
    content: ""; position: absolute; left: 3px; top: 3px;
    width: 8px; height: 8px; border-radius: 50%; background: var(--brand-pink);
  }
  .apps {
    position: absolute; left: 250px; top: 261px;
    display: flex; gap: 26px;
  }
  .app-card { width: 258px; text-align: center; }
  .app-card__media {
    width: 258px; height: 221px; border-radius: 4px;
    box-shadow: 0 6px 16px rgba(0,0,0,0.14);
  }
  .app-card__media--planning { background: linear-gradient(135deg, #4f7fa8, #c9b7a3 55%, #2bb8c4); }
  .app-card__media--tracking { background: linear-gradient(160deg, #b9c2cc, #8d98a6 55%, #5a5f66); }
  .app-card__media--performance { background: linear-gradient(140deg, #3e4c5e, #8b7158 55%, #4a5565); }
  .app-card__title { margin-top: 27px; font-size: 18px; font-weight: 500; color: var(--text-main); }
</style>
</head>
<body>
  <main class="portal">
    <div class="brand">Vantor Hub</div>

    <div class="user">
      <div class="user__name">Marek Ellison</div>
      <div class="user__email">m.ellison@example.com</div>
    </div>
    <div class="avatar" role="img" aria-label="User profile photo"><span class="avatar__status"></span></div>

    <div class="header-rule"></div>

    <nav class="sidebar">
      <div class="nav-item">
        <svg width="22" height="22" viewBox="0 0 24 24" fill="none" stroke="#fff" stroke-width="1.6" stroke-linejoin="round">
          <path d="M3 11 L12 3 L21 11"/>
          <path d="M5.5 9 V21 H10 V15 H14 V21 H18.5 V9"/>
        </svg>
        Home
      </div>
    </nav>

    <div class="mode-switch">
      <label class="mode-switch__option"><span class="radio radio--checked"></span>ON</label>
      <label class="mode-switch__option"><span class="radio"></span>OFF</label>
    </div>

    <section class="apps">
      <div class="app-card">
        <div class="app-card__media app-card__media--planning" role="img" aria-label="Two workers in hard hats reviewing a folder at a container terminal"></div>
        <div class="app-card__title">Jetty Planning</div>
      </div>
      <div class="app-card">
        <div class="app-card__media app-card__media--tracking" role="img" aria-label="Hand holding a phone with a map, trucks in a yard behind"></div>
        <div class="app-card__title">Jetty Tracking</div>
      </div>
      <div class="app-card">
        <div class="app-card__media app-card__media--performance" role="img" aria-label="Warehouse workers loading boxes into a van"></div>
        <div class="app-card__title">Jetty Port Perfomance</div>
      </div>
    </section>
  </main>
</body>
</html>
```